Overview of Elder Abuse Resources Brochure

We need a 2-page brochure that provides a list of resources for elders in tribal communities in the US and those who care for them. We want it to be simple and easy to read, and easy to see the difference between each resource. We would also like eye-catching images or graphics. Please keep the images on the front, and add any photos or graphics that depict Native American elders. We need both of our logos on the first page, in the far-right column. Please refer to the attached image for our brand colors and a font suggestion. Please keep the three columns on each page, but delete the blank pages in the document.

```html
<!DOCTYPE html>
<html lang="en">
<head>
<meta charset="utf-8">
<title>Services for Elders &amp; People Who Care for Them – Brochure</title>
<link href="https://fonts.googleapis.com/css2?family=Barlow+Condensed:wght@500;600;700&family=Open+Sans:wght@400;600;700&display=swap" rel="stylesheet">
<style>
  :root{
    --teal:#4aa3ab;
    --teal-dark:#3a8f97;
    --rust:#b5554a;
    --cream:#f3efea;
    --white:#ffffff;
    --ink:#2b2b2b;
    --stage:#e6e6e6;
    --gold:#b89460;
  }
  *{box-sizing:border-box;margin:0;padding:0}
  html,body{width:1200px;height:2653px;overflow:hidden}
  body{background:var(--stage);font-family:"Open Sans",Arial,sans-serif;color:var(--ink);position:relative}

  .spread{position:absolute;left:50px;width:1100px;height:853px;display:grid;grid-template-columns:repeat(3,1fr);box-shadow:0 6px 18px rgba(0,0,0,.18)}
  .spread--outside{top:443px}
  .spread--inside{top:1356px}
  .panel{position:relative;overflow:hidden;height:853px}
  .panel--cream{background:var(--cream)}
  .panel--white{background:var(--white)}

  .heading{font-family:"Barlow Condensed","Arial Narrow",sans-serif;font-weight:600;text-transform:uppercase;line-height:1.1}
  .heading--rust{color:var(--rust)}
  .heading--teal{color:var(--teal)}

  .photo{position:absolute;background:linear-gradient(160deg,#6f8a5a 0%,#b79a86 45%,#c9b39b 100%)}
  .photo--elders-group{left:0;top:0;width:100%;height:187px}
  .photo--elder-care{left:50%;top:0;width:50%;height:100%;background:linear-gradient(150deg,#7a3d2a 0%,#c56b4a 40%,#9a4f6a 70%,#3b6e8a 100%)}

  .zigzag{position:absolute;left:0;width:100%;height:34px;background:linear-gradient(90deg,#9fc6c9 0%,#c99189 50%,#9fc6c9 100%)}

  /* Respect panel */
  .respect{position:absolute;left:36px;right:30px;top:212px}
  .respect .heading{font-size:30px;margin-bottom:12px}
  .respect p{font-size:14px;line-height:1.3;margin-bottom:16px}
  .respect .emph{font-weight:700}

  /* Help contact */
  .help{position:absolute;left:32px;width:300px}
  .help__tab{position:relative;z-index:2;display:inline-block;background:var(--rust);color:var(--white);font-family:"Barlow Condensed","Arial Narrow",sans-serif;font-weight:600;font-size:20px;padding:4px 60px 4px 18px;border-radius:0 16px 16px 0;margin-left:-8px}
  .help__box{background:var(--teal);color:var(--white);margin-top:-10px;margin-left:8px;padding:24px 18px 18px 18px;font-size:12.5px;line-height:1.25}
  .help__box p{margin-bottom:10px}
  .help__box .phone{font-size:18px;font-weight:700;letter-spacing:.3px;display:block}
  .help__box strong{font-weight:700}
  .help__box p:last-child{margin-bottom:0}

  /* Mailing panel */
  .rot{position:absolute;writing-mode:vertical-rl;transform:rotate(180deg);font-size:13.5px;line-height:1.25}
  .brand-vertical{right:22px;top:22px;font-family:"Barlow Condensed","Arial Narrow",sans-serif;font-weight:600;color:var(--teal);font-size:20px;letter-spacing:.5px;display:flex;align-items:center;gap:10px;text-transform:uppercase}
  .brand-vertical .mark{width:14px;height:14px;background:var(--teal)}
  .recipient{left:146px;top:420px}
  .recipient b{font-weight:700}
  .web-email{left:290px;top:500px}
  .sender{left:28px;top:650px}
  .tel-fax{left:290px;top:680px}

  /* Cover panel */
  .logos{position:absolute;top:40px;left:0;right:0;display:flex;justify-content:center;align-items:center;gap:22px}
  .logos .divider{width:1px;height:100px;background:#cfc8c0}
  .logo-name{font-family:"Open Sans",Arial,sans-serif;font-weight:700;color:var(--teal);font-size:13px;line-height:1.25;text-align:center;width:120px;display:flex;flex-direction:column;align-items:center;gap:8px}
  .logo-name .dot{width:22px;height:22px;border-radius:50%;background:var(--teal)}
  .logo-name--gold{color:var(--gold)}
  .logo-name--gold .dot{background:var(--gold)}
  .cover-title{position:absolute;top:184px;left:0;right:0;text-align:center}
  .cover-title__kicker{display:flex;align-items:center;justify-content:center;gap:10px;font-size:27px;color:var(--teal)}
  .cover-title__kicker::before,.cover-title__kicker::after{content:"";width:30px;height:2px;background:var(--teal)}
  .cover-title__main{font-size:44px;color:var(--teal);line-height:1}
  .cover-title__sub{font-size:30px;color:var(--rust);line-height:1.05}
  .cover-title__rule{width:280px;height:2px;background:var(--teal);margin:8px auto 0}
  .family-band{position:absolute;top:334px;left:0;width:100%;height:230px;background:var(--teal)}
  .checklist{list-style:none;position:absolute;left:22px;top:20px;color:var(--white);font-weight:600;font-size:14.5px}
  .checklist li{display:flex;align-items:center;gap:8px;height:36px}
  .checklist svg{width:14px;height:14px}
  .pills{position:absolute;top:590px;left:22px;right:22px;display:flex;gap:6px}
  .pill{position:relative;flex:1;color:var(--white);font-size:11.5px;font-weight:600;line-height:1.2;text-align:center;padding:18px 6px 8px;border-radius:12px}
  .pill--teal{background:var(--teal)}
  .pill--rust{background:var(--rust)}
  .pill .bulb{position:absolute;top:-14px;left:50%;margin-left:-14px;width:28px;height:28px;border-radius:50%;background:var(--white);border:2px solid currentColor}
  .pill--teal .bulb{color:var(--teal)}
  .pill--rust .bulb{color:var(--rust)}
  .pill .bulb svg{width:100%;height:100%}
  .cover-note{position:absolute;top:660px;left:0;right:0;text-align:center;font-size:15px;font-weight:600;line-height:1.3}
  .cover-note span{color:var(--rust)}
  .cover-web{position:absolute;top:718px;left:0;right:0;text-align:center;font-size:17px;letter-spacing:3px}
  .cover-web b{font-weight:700}

  /* Stories panel */
  .stories{position:absolute;left:36px;right:30px;top:44px}
  .stories .heading{font-size:26px;margin-bottom:14px}
  .story{display:flex;align-items:center;gap:14px;padding:8px 0;border-bottom:1px dashed #c9c2b9;font-size:13.5px;line-height:1.25}
  .story:last-child{border-bottom:none}
  .story__icon{flex:0 0 52px;height:52px;border-radius:50%;background:var(--rust);box-shadow:0 0 0 3px var(--cream),0 0 0 4px var(--rust)}
  .bottom-block{position:absolute;left:40px;width:300px;bottom:0;height:30px;background:var(--teal)}

  /* Resource cards */
  .resources{position:absolute;left:28px;right:28px;top:40px}
  .resources > .heading{font-size:27px;margin-bottom:10px}
  .resources .subhead{font-size:20px;color:var(--rust);margin-bottom:10px}
  .resources .subhead--tight{margin-bottom:2px;margin-top:18px}
  .resources .subnote{font-family:"Barlow Condensed","Arial Narrow",sans-serif;font-weight:500;font-size:17px;line-height:1.2;margin-bottom:14px}
  .card{background:var(--white);border:2px solid var(--rust);border-radius:10px;padding:10px 14px 10px;margin-bottom:12px;font-size:11.5px;line-height:1.3}
  .card--teal{border-color:var(--teal)}
  .card__title{font-family:"Barlow Condensed","Arial Narrow",sans-serif;font-weight:600;font-size:17px;line-height:1.1;color:var(--rust);margin-bottom:4px}
  .card--teal .card__title{color:var(--teal)}
  .card .label{color:var(--rust);font-weight:700}
  .card .link{color:var(--rust)}
</style>
</head>
<body>

<!-- Outside spread -->
<section class="spread spread--outside" aria-label="Brochure outside">
  <article class="panel panel--cream">
    <div class="photo photo--elders-group" role="img" aria-label="Photo of a group of Native American elders standing together outdoors"></div>
    <div class="respect">
      <h2 class="heading heading--rust">Respect for Elders</h2>
      <p>Do you have concerns about an Elder, maybe you see that they are not taking care of themselves, or family only comes once a month when the Elder has money?</p>
      <p>Is an Elder telling you that they are not treated with respect or that someone is bothering them?</p>
      <p class="emph">These may be signs of Elder abuse, neglect or exploitation.</p>
    </div>
    <div class="help" style="top:520px">
      <span class="help__tab">FOR HELP CONTACT:</span>
      <div class="help__box">
        <p>Elder Help Finder for information on Adult Protective Services<span class="phone">1-800-555-0116</span></p>
        <p><strong style="font-size:14px">If a serious emergency, call 911.</strong></p>
        <p>For mental health support for yourself or an Elder, <strong>call or text 555-0988</strong></p>
        <p>Domestic Violence Hotline<span class="phone">1.800.555.SAFE (7233)</span></p>
      </div>
    </div>
    <div class="zigzag" style="top:776px" role="img" aria-label="Teal and rust zigzag border pattern"></div>
  </article>

  <article class="panel panel--white">
    <div class="rot brand-vertical"><span class="mark"></span>Council for Native Aging</div>
    <div class="rot recipient"><b>Recipient</b><br>Street Address<br>City, ST ZIP Code</div>
    <div class="rot web-email">Website<br>Email</div>
    <div class="rot sender">Company Name<br>Street Address<br>City, ST ZIP</div>
    <div class="rot tel-fax">Tel Telephone<br>Fax Fax</div>
  </article>

  <article class="panel panel--cream">
    <div class="logos">
      <div class="logo-name"><span class="dot"></span>Council for Native Aging</div>
      <span class="divider"></span>
      <div class="logo-name logo-name--gold"><span class="dot"></span>Tribal Elder Justice Network</div>
    </div>
    <div class="cover-title">
      <div class="cover-title__kicker heading">Services for</div>
      <div class="cover-title__main heading">Elders &amp; People</div>
      <div class="cover-title__sub heading">Who Care for Them</div>
      <div class="cover-title__rule"></div>
    </div>
    <div class="family-band">
      <ul class="checklist">
        <li><svg viewBox="0 0 14 14"><circle cx="7" cy="7" r="6" fill="none" stroke="#fff" stroke-width="1.3"/><path d="M4 7.2l2 2 4-4" fill="none" stroke="#fff" stroke-width="1.4"/></svg>My Mother</li>
        <li><svg viewBox="0 0 14 14"><circle cx="7" cy="7" r="6" fill="none" stroke="#fff" stroke-width="1.3"/><path d="M4 7.2l2 2 4-4" fill="none" stroke="#fff" stroke-width="1.4"/></svg>My Father</li>
        <li><svg viewBox="0 0 14 14"><circle cx="7" cy="7" r="6" fill="none" stroke="#fff" stroke-width="1.3"/><path d="M4 7.2l2 2 4-4" fill="none" stroke="#fff" stroke-width="1.4"/></svg>My Sister</li>
        <li><svg viewBox="0 0 14 14"><circle cx="7" cy="7" r="6" fill="none" stroke="#fff" stroke-width="1.3"/><path d="M4 7.2l2 2 4-4" fill="none" stroke="#fff" stroke-width="1.4"/></svg>My Grandchild</li>
        <li><svg viewBox="0 0 14 14"><circle cx="7" cy="7" r="6" fill="none" stroke="#fff" stroke-width="1.3"/><path d="M4 7.2l2 2 4-4" fill="none" stroke="#fff" stroke-width="1.4"/></svg>Myself</li>
      </ul>
      <div class="photo photo--elder-care" role="img" aria-label="Photo of an elderly Native American woman receiving care"></div>
    </div>
    <div class="pills">
      <div class="pill pill--teal"><span class="bulb"><svg viewBox="0 0 28 28"><circle cx="14" cy="12" r="5" fill="none" stroke="currentColor" stroke-width="1.6"/><path d="M12 18h4M12.5 20.5h3" stroke="currentColor" stroke-width="1.6"/></svg></span>Are you caring for an Elder or a Grandchild?</div>
      <div class="pill pill--rust"><span class="bulb"><svg viewBox="0 0 28 28"><circle cx="14" cy="12" r="5" fill="none" stroke="currentColor" stroke-width="1.6"/><path d="M12 18h4M12.5 20.5h3" stroke="currentColor" stroke-width="1.6"/></svg></span>Are you an Elder who needs help staying at home?</div>
    </div>
    <p class="cover-note">These programs and information can<br><span>be a helpful resource.</span></p>
    <p class="cover-web">WWW.<b>NATIVEAGINGCOUNCIL</b>.ORG</p>
    <div class="zigzag" style="top:776px" role="img" aria-label="Teal and rust zigzag border pattern"></div>
  </article>
</section>

<!-- Inside spread -->
<section class="spread spread--inside" aria-label="Brochure inside">
  <article class="panel panel--cream">
    <div class="stories">
      <h2 class="heading heading--teal">Do these stories sound<br>familiar to you?</h2>
      <div class="story"><span class="story__icon" role="img" aria-label="Icon of an elder driving"></span><p>My mother gets lost driving home from the store.</p></div>
      <div class="story"><span class="story__icon" role="img" aria-label="Icon of a grocery basket"></span><p>I need help getting groceries and with chores at home.</p></div>
      <div class="story"><span class="story__icon" role="img" aria-label="Icon of a person sleeping"></span><p>My dad wants to sleep all the time; he doesn't go out with friends anymore. He stopped drumming</p></div>
      <div class="story"><span class="story__icon" role="img" aria-label="Icon of three children"></span><p>My sister is raising 3 grandchildren on her own.</p></div>
      <div class="story"><span class="story__icon" role="img" aria-label="Icon of money"></span><p>My son is disrespecting me. He only comes to visit when my retirement money arrives. He always asks for money.</p></div>
    </div>
    <div class="help" style="top:520px">
      <span class="help__tab">FOR HELP CONTACT:</span>
      <div class="help__box">
        <p>Elder Help Finder for information on Adult Protective Services<span class="phone">1-800-555-0116</span></p>
        <p><strong style="font-size:14px">If a serious emergency, call 911.</strong></p>
        <p>For mental health support for yourself or an Elder, <strong>call or text 555-0988</strong></p>
        <p>Domestic Violence Hotline<span class="phone">1.800.555.SAFE (7233)</span></p>
      </div>
    </div>
    <div class="zigzag" style="top:772px" role="img" aria-label="Teal and rust zigzag border pattern"></div>
    <div class="bottom-block"></div>
  </article>

  <article class="panel panel--white">
    <div class="resources">
      <h2 class="heading heading--teal">Resources for Elders</h2>
      <div class="card">
        <h3 class="card__title">Elder Help Finder</h3>
        <p>https://elderhelpfinder.example.gov/home</p>
        <p><span class="label">Call or Text:</span> 1-800-555-0116<br><span class="label">Email:</span> help@elderhelpfinder.org<br>For help finding support. Ask about services to Tribal Elders.</p>
      </div>
      <div class="card card--teal">
        <h3 class="card__title">Memory Care Call Line</h3>
        <p>(24 hours 7 days a week)</p>
        <p><span class="label">Call:</span> 1-800-555-0139<br>For support for people living with dementia, caregivers, families and the public. Connect with a live person who can provide information, local resources, crisis assistance and emotional support.</p>
      </div>
      <div class="card">
        <h3 class="card__title">Crisis Support Lifeline</h3>
        <p>(24 hours 7 days a week)</p>
        <p>For mental health support,<br><span class="label">call or text 555-0988.</span></p>
      </div>
      <div class="card card--teal">
        <h3 class="card__title">State &amp; Tribal Hotlines | Tribal Elder Justice Network</h3>
        <p>To find local resources within your tribe or state that specialize in elder abuse, neglect or exploitation, visit:<br><span class="link">https://nativeagingcouncil.org/tejn/hotlines-codes/state-tribal-hotlines/</span></p>
      </div>
      <div class="card">
        <h3 class="card__title">Circle of Care Native Helpline</h3>
        <p>A 24/7 safe, confidential and anonymous domestic and sexual violence helpline for Native Americans and Alaska Natives.<br><span class="label">Call</span> 1-844-555-0148<br><span class="link">(1-844-555-CARE)<br>https://circleofcarehelpline.org/</span></p>
      </div>
    </div>
  </article>

  <article class="panel panel--cream">
    <div class="resources">
      <h2 class="heading heading--teal">Resources for Caregivers</h2>
      <h3 class="heading subhead">Caring for an Older Adult</h3>
      <div class="card">
        <h3 class="card__title">Elder Help Finder</h3>
        <p>https://elderhelpfinder.example.gov/home</p>
        <p><span class="label">Call or Text:</span> 1-800-555-0116<br><span class="label">Email:</span> help@elderhelpfinder.org<br>For help finding support. Ask about services to Tribal Elders</p>
      </div>
      <div class="card card--teal">
        <h3 class="card__title">Memory Allies | Council for Native Aging</h3>
        <p>An interactive educational program to better understand what dementia is and how it affects people.<br><span class="link">https://nativeagingcouncil.org/memory-allies/</span></p>
      </div>
      <h3 class="heading subhead subhead--tight">Caring for a Grandchild</h3>
      <p class="subnote">Grandparents Raising Grandchildren<br>(Kinship Care)</p>
      <div class="card">
        <h3 class="card__title">Kinfamilies.org</h3>
        <p>An interactive website that seeks to share all relevant publicly available information impacting grandfamilies</p>
      </div>
      <div class="card card--teal">
        <h3 class="card__title">Grandparent Resources | Tribal Elder Justice Network</h3>
        <p>A list of resources for grandparents raising grandchildren<br><span class="link">https://nativeagingcouncil.org/tejn/resource/grandparent-resources/</span></p>
      </div>
    </div>
    <div class="zigzag" style="top:772px" role="img" aria-label="Teal and rust zigzag border pattern"></div>
  </article>
</section>

</body>
</html>
```